Book cover - Rise Above Unease and Bashful Nerves

Book cover for Ebook (Lumora) and wrap around print cover (Printvale) (back, front, and spine)

The book title (may slightly change by end of brief):
(MAIN TITLE) 'Rise Above Unease and Bashful Nerves'
(SUB HEADING) 'A Clear Daily Workbook Guide to Rise Above Unease, Outgrow Timidity and Build Inner Poise'
by Dr Owen Farrby

I would like a bold, stand out cover. Contemporary. I would like to avoid stereotypical images of people looking anxious or worried. I would like the design to be more uplifting and hopeful, rather than focusing on the negative aspect of anxiety, but avoiding cliched photos of people raising their hands in the air, smiling and jumping etc. The cover should appeal to both men and women.

Trim size of book cover (for PrintVale) is 5.25" x 8" back and front with a spine size of 0.477 inches

Reason: I have decided to extend the deadline by 1 more day, not because I am unhappy with the quality of the designs, but because a few designers have contacted me to explain they have had technical difficulties when submitting their files. Thanks everyone for the hard work and great designs.

Target Market(s)

Males and females (16+) who struggle with social anxiety and shyness

Industry/Entity Type

Social

Font styles to use
Serif

Requirements
Must have
• Bold cover that is modern and contemporary. For example, I like these covers:
• http://qvlk.io/8kTz3Pm
• http://qvlk.io/9wHe5Nb
• http://qvlk.io/4jMr7Yc
• http://qvlk.io/6nGs2Lq
• http://qvlk.io/3fVb81t
• http://qvlk.io/7yKd4Ue
• http://qvlk.io/5hWx9Oa
Nice to have
• Open to abstract designs.
Should not have
• No stereotypical pictures of people who look anxious or worried. Avoid cliched photos of people raising their hands in the air, smiling and jumping etc.

```html
<!DOCTYPE html>
<html lang="en">
<head>
<meta charset="utf-8">
<title>Rise Above Unease and Bashful Nerves — Book Cover</title>
<link rel="stylesheet" href="https://fonts.googleapis.com/css2?family=Cinzel:wght@400;500&family=Cabin:wght@400&display=swap">
<style>
  :root {
    --page-bg: #ffffff;
    --cover-bg: #ffffff;
    --cover-edge: #3a3a3a;
    --title-crimson: #c0134a;
    --subtitle-green: #0d6a45;
    --author-ink: #111111;
    --gold-deep: #f0a81c;
    --gold-light: #ffe07a;
    --art-light: #fff27a;
    --art-mid: #ffd62a;
    --art-deep: #f6b21e;
  }
  * { margin: 0; padding: 0; box-sizing: border-box; }
  html, body {
    width: 1200px; height: 1200px; overflow: hidden;
    background: var(--page-bg);
  }
  .canvas { position: relative; width: 1200px; height: 1200px; }
  .book-cover {
    position: absolute; left: 401px; top: 345px;
    width: 324px; height: 494px;
    background: var(--cover-bg);
    border: 1px solid var(--cover-edge);
    overflow: hidden;
  }
  .gold-band {
    position: absolute; left: 0; width: 100%; height: 17px;
    background: linear-gradient(90deg, var(--gold-deep), var(--gold-light) 50%, var(--gold-deep));
  }
  .gold-band--top { top: 0; }
  .gold-band--bottom { bottom: 0; }
  .title {
    position: absolute; left: 0; top: 27px; width: 100%;
    text-align: center;
    font-family: "Cinzel", serif; font-weight: 400;
    color: var(--title-crimson);
    line-height: 1;
  }
  .title span { display: block; }
  .title .small { font-size: 34px; letter-spacing: 0.5px; }
  .title .large { font-size: 52px; margin-top: -2px; }
  .title .medium { font-size: 40px; margin-top: -1px; }
  .subtitle {
    position: absolute; left: 0; top: 186px; width: 100%;
    text-align: center;
    font-family: "Cabin", sans-serif; font-size: 14px;
    line-height: 16.5px;
    color: var(--subtitle-green);
  }
  .hero-art {
    position: absolute; left: 75px; top: 242px;
    width: 182px; height: 184px;
    border-radius: 6px;
    background: linear-gradient(160deg, var(--art-light), var(--art-mid) 55%, var(--art-deep));
  }
  .author {
    position: absolute; left: 0; top: 432px; width: 100%;
    text-align: center;
    font-family: "Cinzel", serif; font-weight: 400;
    font-size: 34px; color: var(--author-ink);
    letter-spacing: 0.3px;
  }
</style>
</head>
<body>
<div class="canvas">
  <div class="book-cover">
    <div class="gold-band gold-band--top"></div>

    <h1 class="title">
      <span class="small">RISE ABOVE</span>
      <span class="large">UNEASE</span>
      <span class="medium">AND BASHFUL</span>
      <span class="small">NERVES</span>
    </h1>

    <p class="subtitle">A Clear Daily Workbook Guide<br>to Rise Above Unease, Outgrow<br>Timidity and Build Inner Poise</p>

    <div class="hero-art" role="img" aria-label="Cheerful yellow emoticon illustration"></div>

    <p class="author">Dr Owen Farrby</p>

    <div class="gold-band gold-band--bottom"></div>
  </div>
</div>
</body>
</html>
```